" Quintela advogados é um escritório de advocacia de grande porte atuando em 6 Estados, sendo em 3 deles temos filial em funcionamento, além da matriz (Curitiba). "

```html
<!DOCTYPE html>
<html lang="pt-BR">
<head>
<meta charset="utf-8">
<title>Quintela Advogados – Placa de identificação</title>
<link rel="stylesheet" href="https://fonts.googleapis.com/css2?family=Open+Sans:wght@400;600;700&display=swap">
<style>
  :root {
    --bg: #e9e7e3;
    --navy-top: #222b38;
    --navy-bottom: #0d131b;
    --white: #ffffff;
    --ink: #1c222b;
    --gold-light: #f2c46a;
    --gold: #c98f2a;
    --gold-dark: #8a5a12;
  }
  * { margin: 0; padding: 0; box-sizing: border-box; }
  html, body { width: 1200px; height: 1200px; overflow: hidden; }
  body {
    background: var(--bg);
    font-family: "Open Sans", Arial, sans-serif;
    position: relative;
  }
  .nameplate {
    position: absolute;
    left: 100px;
    top: 490px;
    width: 1000px;
    height: 220px;
    display: flex;
    box-shadow: 0 14px 30px rgba(0,0,0,0.25);
    border-bottom-left-radius: 46px;
    overflow: hidden;
  }
  .brand-panel {
    width: 505px;
    height: 100%;
    background: linear-gradient(180deg, var(--navy-top), var(--navy-bottom));
    display: flex;
    align-items: center;
    padding-left: 50px;
    gap: 22px;
  }
  .brand-mark {
    width: 62px;
    height: 62px;
    background: linear-gradient(135deg, var(--gold-light), var(--gold-dark));
    flex: none;
  }
  .brand-name {
    color: var(--white);
    font-weight: 400;
    line-height: 1;
  }
  .brand-name .firm { display: block; font-size: 44px; letter-spacing: 2px; }
  .brand-name .area { display: block; font-size: 13px; letter-spacing: 7px; margin-top: 8px; text-align: center; }
  .contact-panel {
    flex: 1;
    background: var(--white);
    position: relative;
    padding: 12px 48px 0 0;
    text-align: right;
    color: var(--ink);
  }
  .gold-edge {
    position: absolute;
    right: 0; top: 0;
    width: 20px; height: 100%;
    background: linear-gradient(90deg, var(--gold-dark), var(--gold-light) 45%, var(--gold));
  }
  .person { font-weight: 700; font-size: 23px; line-height: 1.2; }
  .registration { font-weight: 600; font-size: 12px; margin-bottom: 20px; }
  .contact-list { list-style: none; }
  .contact-list li {
    display: flex;
    justify-content: flex-end;
    align-items: center;
    gap: 8px;
    font-weight: 600;
    font-size: 18px;
    height: 31px;
  }
  .contact-list svg { width: 20px; height: 20px; flex: none; }
</style>
</head>
<body>
  <div class="nameplate">
    <div class="brand-panel">
      <div class="brand-mark"></div>
      <div class="brand-name">
        <span class="firm">QUINTELA</span>
        <span class="area">ADVOGADOS</span>
      </div>
    </div>
    <div class="contact-panel">
      <p class="person">Nome Sobrenome</p>
      <p class="registration">OAB 12345-8</p>
      <ul class="contact-list">
        <li>+55 11 4455-6677
          <svg viewBox="0 0 20 20" fill="none" stroke="#1c222b" stroke-width="1.5"><circle cx="10" cy="10" r="8.5"/><path d="M7 5.5l1.6 2.3-1 1.2a6 6 0 0 0 3.4 3.4l1.2-1 2.3 1.6-.8 1.5c-3.8 0-7.7-3.9-7.7-7.7z" fill="#1c222b"/></svg>
        </li>
        <li>@contato.com.br
          <svg viewBox="0 0 20 20"><rect x="1.5" y="4" width="17" height="12" fill="#1c222b"/><path d="M1.5 4.5l8.5 6.5 8.5-6.5" fill="none" stroke="#fff" stroke-width="1.3"/></svg>
        </li>
        <li>R. exemplo Nº 11 - cidade
          <svg viewBox="0 0 20 20" fill="none" stroke="#1c222b" stroke-width="2"><circle cx="10" cy="10" r="7"/></svg>
        </li>
        <li>site.com.br
          <svg viewBox="0 0 20 20" fill="none" stroke="#1c222b" stroke-width="1.4"><circle cx="10" cy="10" r="8"/><ellipse cx="10" cy="10" rx="3.5" ry="8"/><path d="M2 10h16M3.5 6h13M3.5 14h13"/></svg>
        </li>
      </ul>
      <div class="gold-edge"></div>
    </div>
  </div>
</body>
</html>
```